Home Services- Spring Clean Options

Brightfold Services provides a variety of Home Services- focused on cleaning & improving the exterior of the home:

 Power Washing- driveways, sidewalks, patios, decks, fence
 Fence Staining- make fence look new with variety of staining colors
 Gutter cleaning- important to make sure have proper Water Drainage
 Gutter Guard Installation- prevent damage to roof and house by keeping debris out of gutters and water flowing.
 Window Washing- our exterior washing team and reach the highest windows
 Landscape& Patio Lights- highlight areas for beauty and safety
Updates

We are are almost finished. Just please make sure you pay attention to the wording and grammer in Red thx

Target Market(s)

Middle to Upper level Home Owners (especially women)

Industry/Entity Type

Cleaning Services

Font styles to use
Serif
Sans Serif

Requirements
Must have
• Not be Cluttered- Clean friendly, professional look. Focus on the Professional

Info@TryBrightfoldServices.com
845-267-0000
Nice to have
• Pictures of services- these are just examples
Should not have
• Bigger and bolder Services & Specials. Want to Show all the Services we offer but do Not use too much detail- don't want it to look "cluttered"

```html
<!DOCTYPE html>
<html lang="en">
<head>
<meta charset="utf-8">
<title>Spring Clean Home Services Flyer</title>
<link rel="stylesheet" href="https://fonts.googleapis.com/css2?family=Open+Sans:wght@300;400;600;700;800&display=swap">
<style>
  :root {
    --sky: #29a9e1;
    --indigo: #3a3592;
    --royal: #2e7fcc;
    --ink: #555a60;
    --white: #ffffff;
    --backdrop: #d9d9d9;
    --photo-dark: #2a3326;
    --photo-mid: #4f6a3e;
    --photo-light: #8c8f84;
  }
  * { box-sizing: border-box; margin: 0; padding: 0; }
  html, body { width: 1200px; height: 1200px; overflow: hidden; }
  body {
    background: var(--backdrop);
    font-family: "Open Sans", Arial, sans-serif;
    position: relative;
  }
  .flyer {
    position: absolute;
    left: 152px; top: 20px;
    width: 896px; height: 1160px;
    background: var(--white);
    overflow: hidden;
  }
  .hero-photo {
    position: absolute; left: 0; top: 0;
    width: 896px; height: 640px;
    background: linear-gradient(160deg, var(--photo-dark) 0%, var(--photo-mid) 45%, var(--photo-light) 75%, var(--photo-mid) 100%);
  }
  .headline {
    position: absolute; left: 0; top: 18px; width: 864px;
    text-align: center;
    color: var(--white);
    font-weight: 800;
    font-size: 90px;
    line-height: 1.1;
    letter-spacing: 1px;
  }
  .subhead-band {
    position: absolute; left: 115px; top: 107px;
    width: 634px; height: 65px;
    background: var(--sky);
    color: var(--white);
    font-weight: 700;
    font-size: 50px;
    line-height: 65px;
    letter-spacing: 17px;
    text-align: center;
    padding-left: 17px;
  }
  .shapes { position: absolute; left: 0; top: 0; }
  .intro {
    position: absolute; left: 474px; top: 582px;
    color: var(--white);
    font-size: 31px;
    line-height: 31px;
    text-transform: uppercase;
  }
  .intro .light { font-weight: 300; display: block; }
  .intro .strong { font-weight: 800; display: block; }
  .focus-strip {
    position: absolute; left: 432px; top: 718px;
    width: 464px; height: 60px;
    background: var(--sky);
    box-shadow: 0 6px 10px rgba(0,0,0,0.25);
    color: var(--white);
    font-weight: 600;
    font-size: 19px;
    line-height: 20px;
    padding: 10px 0 0 42px;
    text-transform: uppercase;
  }
  .service {
    position: absolute;
    width: 200px;
    text-align: center;
  }
  .service-photo {
    width: 140px; height: 140px;
    margin: 0 auto;
    border-radius: 50%;
    border: 6px solid var(--indigo);
  }
  .service-photo.ring-sky { border-color: var(--sky); }
  .service-photo.ring-white { border-color: var(--white); }
  .photo-washing { background: linear-gradient(170deg, #6f8466, #9aa888 55%, #c4c2b4); }
  .photo-staining { background: linear-gradient(135deg, #a8561d, #d79a4e 55%, #6b6f78); }
  .photo-gutter-clean { background: linear-gradient(180deg, #b9b4a8, #8a7e6a 60%, #d0cbc0); }
  .photo-window { background: linear-gradient(135deg, #c7ccd2, #5d8fbd 55%, #e8d7c8); }
  .photo-guard { background: linear-gradient(160deg, #e1a548, #9da6ad 55%, #5c6770); }
  .photo-lights { background: linear-gradient(180deg, #1c2a28, #415a3e 55%, #8b6f55); }
  .service-name {
    margin-top: 12px;
    color: var(--sky);
    font-weight: 800;
    font-size: 16px;
    line-height: 17px;
    text-transform: uppercase;
  }
  .service-text {
    margin-top: 6px;
    color: var(--ink);
    font-size: 13.5px;
    line-height: 15.7px;
  }
  .service.on-panel .service-name,
  .service.on-panel .service-text { color: var(--white); }
  .footer-band {
    position: absolute; left: 0; top: 1107px;
    width: 896px; height: 53px;
    background: var(--sky);
    color: var(--white);
    text-align: center;
    font-size: 22px;
    line-height: 53px;
  }
  .footer-band strong { font-weight: 700; }
</style>
</head>
<body>
  <main class="flyer">
    <div class="hero-photo" role="img" aria-label="Family sharing a meal at an outdoor kitchen with a grill on a clean stone patio, surrounded by garden greenery"></div>

    <h1 class="headline">SPRING CLEAN</h1>
    <div class="subhead-band">HOME SERVICES</div>

    <svg class="shapes" width="896" height="1160" viewBox="0 0 896 1160" aria-hidden="true">
      <defs>
        <linearGradient id="panelGradient" x1="0" y1="0" x2="0.3" y2="1">
          <stop offset="0" stop-color="var(--indigo)"/>
          <stop offset="1" stop-color="var(--royal)"/>
        </linearGradient>
        <clipPath id="belowCurve">
          <path d="M0 637 C 220 542, 560 492, 896 620 L 896 1160 L 0 1160 Z"/>
        </clipPath>
      </defs>
      <path d="M0 615 C 220 520, 560 470, 896 598 L 896 1160 L 0 1160 Z" fill="var(--sky)"/>
      <path d="M0 637 C 220 542, 560 492, 896 620 L 896 1160 L 0 1160 Z" fill="var(--white)"/>
      <rect x="447" y="480" width="449" height="627" fill="url(#panelGradient)" clip-path="url(#belowCurve)"/>
    </svg>

    <h2 class="intro">
      <span class="light">Brightfold</span>
      <span class="light">Services provides</span>
      <span class="strong">A variety of</span>
      <span class="strong">Home services</span>
    </h2>
    <div class="focus-strip">Focused on cleaning &amp; improving<br>the exterior of the home</div>

    <section class="service" style="left:2px; top:608px;">
      <div class="service-photo photo-washing" role="img" aria-label="Pressure washer cleaning a concrete driveway"></div>
      <h3 class="service-name">Power Washing</h3>
      <p class="service-text">Driveways, sidewalks,<br>patios, decks, fence</p>
    </section>

    <section class="service" style="left:223px; top:608px;">
      <div class="service-photo photo-staining" role="img" aria-label="Gloved hand applying stain to a wooden fence"></div>
      <h3 class="service-name">Fence Staining</h3>
      <p class="service-text">Make fence look new<br>with variety of<br>staining colors</p>
    </section>

    <section class="service" style="left:2px; top:851px;">
      <div class="service-photo photo-gutter-clean ring-sky" role="img" aria-label="Gloved hand clearing leaves and debris from a gutter"></div>
      <h3 class="service-name">Gutter Cleaning</h3>
      <p class="service-text">Important to make<br>sure have proper<br>water drainage</p>
    </section>

    <section class="service" style="left:223px; top:851px;">
      <div class="service-photo photo-window" role="img" aria-label="Worker washing an exterior window"></div>
      <h3 class="service-name">Window Washing</h3>
      <p class="service-text">Our exterior washing<br>team and reach the<br>highest windows</p>
    </section>

    <section class="service on-panel" style="left:446px; top:806px;">
      <div class="service-photo photo-guard ring-white" role="img" aria-label="Mesh gutter guard installed along a roof edge"></div>
      <h3 class="service-name">Gutter Guard<br>Installation</h3>
      <p class="service-text">Prevent damage to<br>roof and house by<br>keeping debris out of<br>gutters and<br>water flowing.</p>
    </section>

    <section class="service on-panel" style="left:667px; top:806px;">
      <div class="service-photo photo-lights ring-white" role="img" aria-label="String lights glowing over a patio at dusk"></div>
      <h3 class="service-name">Landscape &amp;<br>Patio Lights</h3>
      <p class="service-text">Highlight areas for<br>beauty and safety</p>
    </section>

    <footer class="footer-band">www.<strong>brightfoldservices</strong>.com</footer>
  </main>
</body>
</html>
```